Forge Night Club Flyer, need asap for party this weekend

Need a flyer for club night this Saturday. Guaranteed project need quick turnaround. Image attached, and the FORGE logo to be large and detailed like a sign. The dj names MERIDAN, MR. KALTOVE, AND DESMOND R. FALLOWAY can be large too. It's for house/electronic music in a nice classy venue. High Res image attached.

Target Market(s)

21-40 year old house music lovers, club business

Industry/Entity Type

Night Club

Font styles to use
Sans Serif

Colors
ffffff
cadf82
33a6d7
0356a4
fbee3d

Requirements
Must have
• Either the girl in hard hat or tool belt image, or something similar to stick with the Forge theme. Also the dj names needs to be the same size
Nice to have
• Faded image or some lining around the images so it doesn't look like a plain photo. Black and white is good or faded.
Should not have
• Any cursive or anything not professional looking

```html
<!DOCTYPE html>
<html lang="en">
<head>
<meta charset="utf-8">
<title>Forge Club Night Flyer</title>
<link href="https://fonts.googleapis.com/css2?family=Bebas+Neue&family=Oswald:wght@400;500&family=Jost:ital,wght@0,600;1,600&display=swap" rel="stylesheet">
<style>
  :root{
    --white:#ffffff;
    --lime:#cadf82;
    --sky:#33a6d7;
    --navy:#0356a4;
    --yellow:#fbee3d;
    --haze:#bcc6e8;
    --stage:#ececec;
    --title:#e6e9f1;
    --title-shade:#1f4f9c;
    --name-edge:#4a5a3a;
  }
  html,body{margin:0;padding:0;overflow:hidden;}
  body{width:1200px;height:675px;background:var(--stage);position:relative;}
  .flyer{
    position:absolute;left:348px;top:10px;width:504px;height:655px;
    background:var(--white);
  }
  .flyer svg{display:block;width:100%;height:100%;}
  .title{font-family:"Bebas Neue",sans-serif;fill:var(--title);}
  .title-shade{font-family:"Bebas Neue",sans-serif;fill:var(--title-shade);}
  .tagline{font-family:"Oswald",sans-serif;font-weight:500;fill:var(--white);}
  .dj-label{font-family:"Oswald",sans-serif;font-weight:500;fill:var(--white);}
  .dj-name{
    font-family:"Bebas Neue",sans-serif;fill:var(--yellow);
    stroke:var(--name-edge);stroke-width:2;paint-order:stroke;
  }
  .event-date{font-family:"Jost",sans-serif;font-weight:600;fill:var(--white);}
  .event-time{font-family:"Jost",sans-serif;font-weight:600;font-style:italic;fill:var(--white);}
  .venue{font-family:"Jost",sans-serif;font-weight:600;fill:var(--white);letter-spacing:2px;}
</style>
</head>
<body>
  <div class="flyer">
    <svg viewBox="0 0 600 780" xmlns="http://www.w3.org/2000/svg">
      <defs>
        <clipPath id="flyer-area"><rect x="6" y="6" width="588" height="768"/></clipPath>
        <linearGradient id="photo-tone" x1="0" y1="0" x2="1" y2="1">
          <stop offset="0" stop-color="#9aa4d2"/>
          <stop offset="0.5" stop-color="#6a78b6"/>
          <stop offset="1" stop-color="#3f5592"/>
        </linearGradient>
      </defs>
      <g clip-path="url(#flyer-area)">
        <rect class="backdrop" x="6" y="6" width="588" height="768" fill="var(--haze)"/>
        <rect class="hero-photo" x="6" y="6" width="330" height="600" fill="url(#photo-tone)"
              role="img" aria-label="Faded blue-toned photo of a worker's waist wearing a tool belt with wrenches and pliers"/>
        <g class="bands" opacity="0.92">
          <polygon class="band band-yellow" points="405,20 1008,774 -198,774" fill="var(--yellow)"/>
          <polygon class="band band-lime" points="405,75 921,720 -111,720" fill="var(--lime)"/>
          <polygon class="band band-sky" points="405,130 839,672 -29,672" fill="var(--sky)"/>
          <polygon class="band band-navy" points="405,190 751,622 59,622" fill="var(--navy)"/>
        </g>
        <rect class="photo-frame" x="12" y="12" width="318" height="588" fill="none" stroke="var(--white)" stroke-width="2" opacity="0.7"/>
        <circle class="event-badge" cx="382" cy="622" r="112" fill="var(--sky)"/>
      </g>

      <text class="title-shade" x="401" y="182" text-anchor="middle" font-size="176" letter-spacing="2">FORGE</text>
      <text class="title" x="405" y="178" text-anchor="middle" font-size="176" letter-spacing="2">FORGE</text>
      <text class="tagline" x="262" y="212" font-size="24">HOUSE &amp; TECH WORKERS</text>

      <text class="dj-label" x="262" y="250" font-size="22">DJ'S</text>
      <g class="hazard-stripes" fill="var(--yellow)">
        <polygon points="322,254 334,254 342,232 330,232"/>
        <polygon points="344,254 356,254 364,232 352,232"/>
        <polygon points="366,254 378,254 386,232 374,232"/>
        <polygon points="388,254 400,254 408,232 396,232"/>
        <polygon points="410,254 422,254 430,232 418,232"/>
        <polygon points="432,254 444,254 452,232 440,232"/>
        <polygon points="454,254 466,254 474,232 462,232"/>
        <polygon points="476,254 488,254 496,232 484,232"/>
      </g>

      <text class="dj-name" x="262" y="332" font-size="60">MERIDAN</text>
      <text class="dj-name" x="262" y="394" font-size="60">MR. KALTOVE</text>
      <text class="dj-name" x="572" y="456" font-size="60" text-anchor="end">DESMOND R. FALLOWAY</text>

      <text class="event-date" x="382" y="568" font-size="20" text-anchor="middle">SAT 3/12/16</text>
      <text class="event-time" x="382" y="592" font-size="20" text-anchor="middle">10PM - 2AM</text>
      <text class="venue" x="382" y="630" font-size="19" text-anchor="middle">418 N LARKSPUR</text>
      <text class="venue" x="382" y="652" font-size="19" text-anchor="middle">AVE, ELMWOOD</text>
    </svg>
  </div>
</body>
</html>
```